Door Hanger / Brochure / Work Estimate Sheet
Brightwell Scrubbing & Remodel Services
pelund - if the design was not submitted it cannot be considered for final judgement.
A winner has been selected. They will be notified shortly.
wendal, had this marvelous design, but just when i was about to upload, my network went down. what happens now?
Contest is extended for 2 more days.
-Pam
The designs are looking great so far. Just to clarify:
1. I would like to see a 3 fold brochure.
2. I would like to have something that looks like "stik-em" notes pasted on the brochure. I will be uploading an example of what I'm talking about. I DO NOT want to copy the template that I'm uploading I just want to see the "stik-em" notes on the brochure.
3. On the back panel, I would like to see a check-list that a customer could check off some of the items that they would like done in their home.

```html
<!DOCTYPE html>
<html lang="en">
<head>
<meta charset="utf-8">
<title>Brightwell Scrubbing &amp; Remodel Services – Brochure and Door Hanger</title>
<link rel="stylesheet" href="https://fonts.googleapis.com/css2?family=Open+Sans:ital,wght@0,400;0,600;0,700;1,700&amp;display=swap">
<style>
  :root {
    --bg: #ece9e4;
    --blue: #1f5fa8;
    --blue-dark: #163f73;
    --blue-light: #4f8fd0;
    --green: #7bbf3a;
    --green-dark: #4f8f22;
    --paper: #ffffff;
    --text: #2d3440;
    --muted: #6b7480;
    --photo-warm: #c9a67e;
    --photo-cool: #a9b9c8;
  }
  * { box-sizing: border-box; margin: 0; padding: 0; }
  html, body { width: 1200px; height: 756px; overflow: hidden; }
  body { background: var(--bg); font-family: "Open Sans", Arial, sans-serif; color: var(--text); position: relative; }

  .sheet { position: absolute; background: var(--paper); box-shadow: 0 2px 8px rgba(0,0,0,.15); display: flex; }
  .brochure-outside { left: 30px; top: 30px; width: 560px; height: 320px; }
  .brochure-inside { left: 30px; top: 380px; width: 560px; height: 320px; }
  .panel { flex: 1; position: relative; overflow: hidden; border-right: 1px solid #e3e6ea; }
  .panel:last-child { border-right: none; }

  .photo { position: absolute; }
  .photo-warm { background: linear-gradient(135deg, #e3cfb4, var(--photo-warm)); }
  .photo-cool { background: linear-gradient(135deg, #dfe7ef, var(--photo-cool)); }
  .photo-mix { background: linear-gradient(160deg, #f1e3cf, #b6c7d8); }

  .heading { font-size: 11px; font-weight: 700; color: var(--blue); text-transform: uppercase; }
  .body-copy { font-size: 8px; line-height: 1.5; color: var(--muted); }
  .band { position: absolute; left: 0; right: 0; background: linear-gradient(90deg, var(--blue-dark), var(--blue-light)); color: #fff; }
  .band-title { font-size: 9px; font-weight: 700; text-transform: uppercase; padding: 4px 10px; background: var(--green); display: inline-block; border-radius: 0 10px 10px 0; margin-top: 6px; }
  .service-list { list-style: none; padding: 6px 12px; font-size: 8px; line-height: 1.7; }
  .service-list li::before { content: ""; display: inline-block; width: 5px; height: 5px; background: var(--green); margin-right: 6px; vertical-align: middle; }
  .check-list li::before { width: 7px; height: 7px; background: #fff; border: 1px solid var(--blue); }

  .brand { display: flex; align-items: center; gap: 6px; }
  .brand-mark { width: 14px; height: 14px; background: var(--blue); }
  .brand-name { font-size: 15px; font-weight: 700; color: var(--blue); text-transform: uppercase; }
  .tagline { font-size: 7px; font-weight: 700; color: var(--blue); text-transform: uppercase; line-height: 1.4; }
  .web { font-size: 8px; font-weight: 600; color: var(--blue); }
  .green-curve { position: absolute; left: 0; width: 100%; }

  .hanger { position: absolute; top: 30px; width: 220px; height: 620px; background: var(--paper); box-shadow: 0 2px 8px rgba(0,0,0,.15); border-radius: 6px; overflow: hidden; }
  .hanger-front { left: 680px; }
  .hanger-back { left: 930px; }
  .hanger-hole { position: absolute; top: 28px; left: 50%; width: 90px; height: 90px; margin-left: -45px; border-radius: 50%; background: var(--bg); }
  .hanger-slit { position: absolute; top: 0; left: 50%; width: 8px; height: 40px; margin-left: -4px; background: var(--bg); }

  .caption { position: absolute; font-size: 11px; font-weight: 700; font-style: italic; color: #3a3a3a; text-transform: uppercase; line-height: 1.3; }
</style>
</head>
<body>

<!-- Brochure outside -->
<section class="sheet brochure-outside">
  <div class="panel">
    <div class="photo photo-warm" style="left:0;top:0;width:100%;height:110px" role="img" aria-label="Photo of a bright, clean living room"></div>
    <div style="position:absolute;left:14px;top:124px;right:14px">
      <p class="heading">About Us</p>
      <p class="body-copy" style="margin-top:6px">We clean, repair and refresh homes across the region with care, skill and honest pricing on every job.</p>
    </div>
    <svg class="green-curve" style="bottom:0" height="60" viewBox="0 0 186 60" preserveAspectRatio="none"><path d="M0 30 Q90 0 186 24 V60 H0Z" fill="var(--green)"/><path d="M0 42 Q90 14 186 36 V60 H0Z" fill="var(--blue)"/></svg>
  </div>
  <div class="panel">
    <div class="photo photo-warm" style="left:0;top:0;width:100%;height:170px" role="img" aria-label="Photo of a smiling baby on a soft carpet"></div>
    <div style="position:absolute;left:14px;top:186px;right:14px">
      <p class="body-copy">Call today for a free estimate on any room in your home.</p>
      <div class="brand" style="margin-top:14px"><span class="brand-mark"></span><span class="brand-name" style="font-size:12px">Brightwell</span></div>
    </div>
  </div>
  <div class="panel">
    <div class="photo" style="right:0;top:0;width:60px;height:40px;background:linear-gradient(135deg,#a6d36d,var(--green))" role="img" aria-label="Green leaf decoration"></div>
    <div style="position:absolute;left:16px;top:52px">
      <div class="brand"><span class="brand-mark"></span><span class="brand-name">Brightwell</span></div>
      <p class="tagline" style="margin-top:8px">Home Improvement &amp; Renovation<br>Services Provider</p>
    </div>
    <div class="photo photo-warm" style="left:0;top:140px;width:100%;height:140px" role="img" aria-label="Photo of three smiling children with a dog"></div>
    <p class="web" style="position:absolute;left:16px;bottom:12px">www.brightwell-home.example</p>
  </div>
</section>

<!-- Brochure inside -->
<section class="sheet brochure-inside">
  <div class="panel">
    <div class="photo photo-mix" style="left:0;top:0;width:100%;height:90px" role="img" aria-label="Photo of a cleaned room interior"></div>
    <div class="band" style="top:96px;height:128px">
      <span class="band-title">Cleaning Services</span>
      <ul class="service-list">
        <li>Carpet Cleaning</li><li>Upholstery Cleaning</li><li>Tile &amp; Grout Cleaning</li><li>Pet Odor Removal</li><li>Stain Treatment</li><li>Area Rug Care</li>
      </ul>
    </div>
    <div class="photo photo-warm" style="left:0;bottom:0;width:100%;height:90px" role="img" aria-label="Photo of a child and a dog lying on a carpet"></div>
  </div>
  <div class="panel">
    <p class="heading" style="position:absolute;left:14px;right:14px;top:16px;font-size:9px;line-height:1.45">Brightwell cleaning &amp; restoration has served Larkfield and area for over 18 years. Let our experience work for you.</p>
    <div class="band" style="top:90px;height:140px">
      <span class="band-title">Home Improvement</span>
      <ul class="service-list">
        <li>Basement Finishing</li><li>Drywall Repair</li><li>Interior Painting</li><li>Flooring Installation</li><li>Kitchen Updates</li><li>Bathroom Renovation</li><li>Custom Trim Work</li>
      </ul>
    </div>
    <div class="photo photo-cool" style="left:0;bottom:0;width:100%;height:80px" role="img" aria-label="Photo of a renovated kitchen"></div>
  </div>
  <div class="panel">
    <div class="photo" style="right:0;top:0;width:60px;height:40px;background:linear-gradient(135deg,#a6d36d,var(--green))" role="img" aria-label="Green leaf decoration"></div>
    <p class="heading" style="position:absolute;left:14px;top:40px">What can we do for you?</p>
    <ul class="service-list check-list" style="position:absolute;left:4px;top:58px;color:var(--text)">
      <li>Carpets</li><li>Windows</li><li>Walls</li><li>Floors</li><li>Cabinets</li><li>Doors</li>
    </ul>
    <div class="photo photo-warm" style="left:0;bottom:0;width:100%;height:120px" role="img" aria-label="Photo of a dog resting in a clean home"></div>
  </div>
</section>

<p class="caption" style="left:30px;top:712px">Brochure<br>Outside/Inside</p>

<!-- Door hanger front -->
<section class="hanger hanger-front">
  <div class="hanger-hole"></div><div class="hanger-slit"></div>
  <div class="brand" style="position:absolute;left:22px;top:140px"><span class="brand-mark"></span><span class="brand-name">Brightwell</span></div>
  <div class="band" style="top:190px;height:190px">
    <span class="band-title" style="margin-top:10px">Cleaning Services</span>
    <ul class="service-list" style="font-size:10px;line-height:1.9">
      <li>Carpet Cleaning</li><li>Upholstery Care</li><li>Tile Cleaning</li><li>Duct Cleaning</li><li>Water Damage</li>
    </ul>
  </div>
  <div class="photo photo-mix" style="left:0;bottom:0;width:100%;height:220px" role="img" aria-label="Photo of a cleaner working in a living room"></div>
</section>

<!-- Door hanger back -->
<section class="hanger hanger-back">
  <div class="hanger-hole"></div><div class="hanger-slit"></div>
  <div style="position:absolute;left:22px;top:140px">
    <div class="brand"><span class="brand-mark"></span><span class="brand-name">Brightwell</span></div>
    <p class="tagline" style="margin-top:8px">Home Improvement &amp; Renovation<br>Services Provider</p>
  </div>
  <ul class="service-list" style="position:absolute;left:10px;top:210px;font-size:10px;line-height:1.9">
    <li>Basement Finishing</li><li>Painting</li><li>Flooring</li><li>Drywall Repair</li><li>Renovations</li>
  </ul>
  <div class="photo photo-warm" style="left:0;top:360px;width:100%;height:210px" role="img" aria-label="Photo of a mother holding a baby at home"></div>
  <p class="web" style="position:absolute;left:0;right:0;bottom:18px;text-align:center;font-size:10px">www.brightwell-home.example</p>
</section>

<p class="caption" style="left:930px;top:665px">Door Hanger<br>Front/Back</p>

</body>
</html>
```